Pemberly property maintenance house wash and water tank cleaning trailer

Pemberly property maintenance is an exterior cleaning company, we have built a new trailer for cleaning water tanks and buildings. We would like a design that incorporates our company name, logo, phone number and web page. The trailer has 11 aluminum panels on it as you will see in the pics, we would like a design that brings it all together. The front 2 corner panels get a bit dirty, so our thought were we might be able to have a design that makes the front of the trailer look dirty and the rest look clean. For example a mud splash in the background on the front panels and maybe the front side panels and then the rest of the panels looking like they are soaped up or clean. www.pemberlypropertymaintenance.co.nz for details

Requirements
Must have
• A design that is eye catching
Nice to have
• some use of our company colors ( see pics or website ) www.pemberlypropertymaintnenance.co.nz

Website across the rear of the trailer
Should not have
• plain design

```html
<!DOCTYPE html>
<html lang="en">
<head>
<meta charset="utf-8">
<title>Pemberly Property Maintenance – Trailer Panel Layout</title>
<link href="https://fonts.googleapis.com/css2?family=Roboto+Condensed:wght@700&family=Stardos+Stencil:wght@700&family=Roboto:wght@400&display=swap" rel="stylesheet">
<style>
  :root {
    --green: #00ad4f;
    --mud: #8a5530;
    --ink: #111111;
    --dim: #222222;
    --frame: #d9d9d9;
    --paper: #ffffff;
  }
  html, body { margin: 0; padding: 0; overflow: hidden; background: var(--paper); }
  .sheet { display: block; width: 1200px; height: 801px; }
  .panel-frame { fill: var(--paper); stroke: var(--frame); stroke-width: 1.5; }
  .panel-green { fill: var(--green); }
  .dimension { font-family: "Roboto", sans-serif; font-size: 11.5px; fill: var(--dim); }
  .dimension-small { font-size: 8.5px; }
  .brand-name { font-family: "Roboto Condensed", sans-serif; font-weight: 700; fill: var(--ink); }
  .brand-square { fill: var(--ink); }
  .web-address { font-family: "Roboto Condensed", sans-serif; font-weight: 700; font-size: 35px; fill: var(--ink); }
  .service-title { font-family: "Stardos Stencil", serif; font-weight: 700; font-size: 14px; fill: var(--ink); }
  .service-item { font-family: "Roboto", sans-serif; font-size: 7.6px; fill: var(--ink); }
  .bullet { fill: var(--ink); }
  .phone-number { font-family: "Stardos Stencil", serif; font-weight: 700; font-size: 38px; fill: var(--ink); letter-spacing: 1px; }
  .phone-icon { fill: none; stroke: var(--ink); stroke-width: 2.4; }
  .social-label { font-family: "Roboto", sans-serif; font-size: 8px; fill: var(--paper); }
  .social-dot { fill: none; stroke: var(--paper); stroke-width: 1.4; }
</style>
</head>
<body>
<svg class="sheet" viewBox="0 0 1200 801" xmlns="http://www.w3.org/2000/svg">
  <defs>
    <linearGradient id="mudToGreen" x1="0" x2="1" y1="0" y2="0">
      <stop offset="0" stop-color="#8a5530"/>
      <stop offset="0.12" stop-color="#7d6a3a"/>
      <stop offset="0.35" stop-color="#00ad4f"/>
    </linearGradient>
    <linearGradient id="mudOnGreen" x1="0" x2="1" y1="1" y2="0">
      <stop offset="0" stop-color="#8a5530"/>
      <stop offset="0.45" stop-color="#3d8d45"/>
      <stop offset="0.8" stop-color="#00ad4f"/>
    </linearGradient>
    <linearGradient id="splatterFade" x1="0" x2="0" y1="0" y2="1">
      <stop offset="0" stop-color="#ffffff"/>
      <stop offset="1" stop-color="#e3d2c2"/>
    </linearGradient>
    <radialGradient id="splatterPanel" cx="0.75" cy="0.6" r="0.8">
      <stop offset="0" stop-color="#d8bfa6"/>
      <stop offset="0.6" stop-color="#efe4da"/>
      <stop offset="1" stop-color="#ffffff"/>
    </radialGradient>
  </defs>

  <!-- Row 1 -->
  <g class="panel nose-name">
    <rect class="panel-frame" x="64" y="51" width="163" height="88"/>
    <rect class="brand-square" x="72" y="88" width="13" height="13"/>
    <text class="brand-name" x="90" y="99" font-size="13" textLength="129" lengthAdjust="spacingAndGlyphs">Pemberly Property Maintenance</text>
  </g>
  <text class="dimension" x="243" y="95" text-anchor="middle" transform="rotate(-90 243 95)">295 mm</text>
  <text class="dimension" x="151" y="152" text-anchor="middle">550 mm</text>

  <text class="dimension" x="616" y="41" text-anchor="middle">2325 mm</text>
  <g class="panel rear-web">
    <rect class="panel-frame" x="271" y="51" width="692" height="88"/>
    <text class="web-address" x="617" y="108" text-anchor="middle" textLength="650" lengthAdjust="spacingAndGlyphs">www.PemberlyPropertyMaintnenance.co.nz</text>
  </g>

  <g class="panel splatter-end">
    <rect class="panel-frame" x="999" y="51" width="163" height="88"/>
    <rect x="1000" y="52" width="161" height="86" fill="url(#splatterPanel)" role="img" aria-label="Mud splatter with soap bubbles"/>
  </g>

  <!-- Row 2 -->
  <text class="dimension" x="318" y="178" text-anchor="middle">1305 mm</text>
  <text class="dimension" x="195" y="218" text-anchor="middle" transform="rotate(-90 195 218)">270 mm</text>
  <g class="panel side-name">
    <polygon points="204,189 590,189 505,276 204,276" fill="url(#mudToGreen)" role="img" aria-label="Mud splash fading into green"/>
    <rect class="brand-square" x="262" y="225" width="18" height="18"/>
    <text class="brand-name" x="287" y="241" font-size="20" textLength="220" lengthAdjust="spacingAndGlyphs">Pemberly Property Maintenance</text>
  </g>
  <text class="dimension" x="322" y="293" text-anchor="middle">1037 mm</text>

  <g class="panel side-water-tank">
    <polygon class="panel-green" points="640,192 1026,192 1026,279 726,279"/>
    <text class="service-title" x="718" y="221">WATER TANK CLEANING</text>
    <circle class="bullet" cx="726" cy="235" r="3"/>
    <text class="service-item" x="734" y="236">Water Tank Clean</text>
    <circle class="bullet" cx="726" cy="248" r="3"/>
    <text class="service-item" x="734" y="249">Water Tank Clean &amp; Sanitize</text>
    <text class="social-label" x="1012" y="252" text-anchor="end">Chatterbook · Tweetly</text>
  </g>

  <!-- Row 3 -->
  <text class="dimension" x="195" y="342" text-anchor="middle" transform="rotate(-90 195 342)">270 mm</text>
  <g class="panel side-exterior">
    <polygon points="204,312 590,312 505,400 204,400" fill="url(#mudToGreen)" role="img" aria-label="Mud splash fading into green"/>
    <text class="service-title" x="285" y="336">EXTERIOR PROPERTY CLEANING</text>
    <circle class="bullet" cx="288" cy="345" r="3"/>
    <text class="service-item" x="296" y="348">Water Blasting</text>
    <circle class="bullet" cx="288" cy="358" r="3"/>
    <text class="service-item" x="296" y="362">House Washing / Soft wash</text>
    <circle class="bullet" cx="288" cy="372" r="3"/>
    <text class="service-item" x="296" y="375">Spouting/ Gutter Clearing</text>
    <circle class="bullet" cx="288" cy="385" r="3"/>
    <text class="service-item" x="296" y="389">Deck Cleaning</text>
  </g>
  <text class="dimension" x="318" y="422" text-anchor="middle">1305 mm</text>

  <g class="panel side-extra-services">
    <polygon class="panel-green" points="640,315 1026,315 1026,403 726,403"/>
    <circle class="bullet" cx="730" cy="337" r="3"/>
    <text class="service-item" x="742" y="340">Moss and Mould Treatment</text>
    <circle class="bullet" cx="730" cy="351" r="3"/>
    <text class="service-item" x="742" y="354">Cleaning Driveways and Paths</text>
    <circle class="bullet" cx="730" cy="364" r="3"/>
    <text class="service-item" x="742" y="367">Sanitize Playground Equipment</text>
    <circle class="bullet" cx="730" cy="378" r="3"/>
    <text class="service-item" x="742" y="381">Sanitize Outdoor Seating</text>
    <circle class="bullet" cx="881" cy="337" r="3"/>
    <text class="service-item" x="892" y="340">Clean Solar Panels</text>
    <circle class="bullet" cx="881" cy="351" r="3"/>
    <text class="service-item" x="892" y="354">Fence Cleaning</text>
  </g>

  <!-- Row 4 -->
  <text class="dimension dimension-small" x="222" y="457" text-anchor="middle" transform="rotate(-90 222 457)">65 mm</text>
  <rect class="panel-green trim-bar" x="227" y="447" width="158" height="21"/>
  <text class="dimension" x="302" y="480" text-anchor="middle">490 mm</text>

  <text class="dimension" x="627" y="423" text-anchor="middle">1030 mm</text>
  <g class="panel phone">
    <rect class="panel-green" x="462" y="433" width="304" height="47"/>
    <circle class="phone-icon" cx="489" cy="457" r="14"/>
    <path d="M483 449 q-3 3 0 9 q4 7 10 8 l3 -3 -4 -3 -2 2 q-4 -2 -5 -6 l2 -2 -3 -4 z" fill="var(--ink)"/>
    <text class="phone-number" x="513" y="471">21 555 0182</text>
  </g>
  <text class="dimension" x="782" y="457" text-anchor="middle" transform="rotate(-90 782 457)">160 mm</text>

  <rect class="panel-green trim-bar" x="837" y="446" width="158" height="21"/>

  <!-- Row 5 -->
  <text class="dimension" x="154" y="508" text-anchor="middle">682 mm</text>
  <text class="dimension" x="40" y="644" text-anchor="middle" transform="rotate(-90 40 644)">880 mm</text>
  <g class="panel front-left">
    <polygon class="panel-frame" points="41,512 243,512 243,772 41,764"/>
    <rect x="42" y="610" width="200" height="60" fill="url(#splatterFade)" role="img" aria-label="Mud splatter on white"/>
    <path d="M42 684 Q140 660 242 664 L242 771 L42 763 Z" fill="url(#mudOnGreen)" role="img" aria-label="Heavy mud splash over green"/>
    <rect class="brand-square" x="50" y="570" width="16" height="16"/>
    <text class="brand-name" x="72" y="585" font-size="17" textLength="162" lengthAdjust="spacingAndGlyphs">Pemberly Property Maintenance</text>
  </g>
  <text class="dimension" x="258" y="644" text-anchor="middle" transform="rotate(-90 258 644)">850 mm</text>

  <g class="panel front-corner-left">
    <polygon class="panel-frame" points="341,509 405,685 407,759 341,759"/>
    <polygon points="342,520 403,685 342,685" fill="url(#splatterFade)" role="img" aria-label="Mud splatter on white"/>
    <path d="M342 667 Q375 669 404 676 L406 758 L342 758 Z" fill="url(#mudOnGreen)" role="img" aria-label="Mud splash over green"/>
  </g>
  <text class="dimension" x="387" y="595" text-anchor="middle" transform="rotate(70 387 595)">580 mm</text>
  <text class="dimension" x="335" y="646" text-anchor="middle" transform="rotate(-90 335 646)">840 mm</text>
  <text class="dimension" x="421" y="723" text-anchor="middle" transform="rotate(-90 421 723)">260 mm</text>
  <text class="dimension" x="373" y="775" text-anchor="middle">210 mm</text>

  <text class="dimension" x="588" y="505" text-anchor="middle">770 mm</text>
  <g class="panel front-centre">
    <rect class="panel-frame" x="470" y="509" width="236" height="168"/>
    <rect x="471" y="510" width="234" height="130" fill="url(#splatterFade)" role="img" aria-label="Light mud splatter on white"/>
    <path d="M471 672 Q570 624 705 614 L705 676 L471 676 Z" class="panel-green"/>
    <rect class="panel-green" x="470" y="682" width="236" height="73"/>
  </g>
  <text class="dimension" x="726" y="610" text-anchor="middle" transform="rotate(-90 726 610)">550 mm</text>
  <text class="dimension" x="726" y="718" text-anchor="middle" transform="rotate(-90 726 718)">285 mm</text>

  <g class="panel front-corner-right">
    <polygon class="panel-frame" points="821,509 821,759 756,759 758,685"/>
    <polygon points="820,520 820,685 759,685" fill="url(#splatterFade)" role="img" aria-label="Mud splatter on white"/>
    <path d="M759 676 Q790 668 820 666 L820 758 L757 758 Z" fill="url(#mudOnGreen)" role="img" aria-label="Mud splash over green"/>
  </g>

  <text class="dimension" x="1022" y="508" text-anchor="middle">682 mm</text>
  <text class="dimension" x="908" y="644" text-anchor="middle" transform="rotate(-90 908 644)">880 mm</text>
  <g class="panel front-right">
    <polygon class="panel-frame" points="912,512 1114,512 1114,764 912,772"/>
    <rect x="913" y="610" width="200" height="60" fill="url(#splatterFade)" role="img" aria-label="Mud splatter on white"/>
    <path d="M913 664 Q1015 662 1113 684 L1113 763 L913 771 Z" fill="url(#mudOnGreen)" role="img" aria-label="Heavy mud splash over green"/>
    <rect class="brand-square" x="921" y="570" width="16" height="16"/>
    <text class="brand-name" x="943" y="585" font-size="17" textLength="162" lengthAdjust="spacingAndGlyphs">Pemberly Property Maintenance</text>
  </g>
  <text class="dimension" x="1126" y="644" text-anchor="middle" transform="rotate(-90 1126 644)">850 mm</text>
</svg>
</body>
</html>
```